Cigar Ring Design

we are working on a project, which is an eCommerce store for cigars, now instead of selling all kind of existing brands this project is based on a TabacoMillDepot concept where an outlet is linked to an actual Cigar factory,
so the cigar lines sold will come out under a TMD (TabacoMillDepot) brand consisting of various labels, (think Barney Cotter, Ochre Crest, Slate Crest etc) I had an idea for the Cigar Rings for this project, where I put TM in an O (circle) of which I made mock ups (see attachement), now I am not a designer, I am sure a real designer can come up with something more stylish and unique.

```html
<!DOCTYPE html>
<html lang="en">
<head>
<meta charset="utf-8">
<title>TMD Cigar Rings</title>
<link rel="stylesheet" href="https://fonts.googleapis.com/css2?family=Cinzel:wght@700&display=swap">
<style>
  :root {
    --gold: #c9a227;
    --gold-light: #f3dc4a;
    --gold-text: #f0d21e;
    --brown-text: #2b1a10;
    --crown-top: #f6e79a;
    --crown-bottom: #b8911d;
  }
  * { box-sizing: border-box; margin: 0; padding: 0; }
  html, body { width: 1200px; height: 1200px; overflow: hidden; background: #fff; }
  .sheet { position: relative; width: 1200px; height: 1200px; }

  .ring {
    position: absolute;
    width: 470px;
    height: 177px;
    overflow: hidden;
    font-family: "Cinzel", Georgia, serif;
    font-weight: 700;
  }
  .ring--umber  { left: 85px;  top: 289px; background: #231c1a; }
  .ring--pewter { left: 646px; top: 292px; background: linear-gradient(#6d6e70, #e6e6e7 50%, #6d6e70); }
  .ring--slate  { left: 85px;  top: 504px; background: linear-gradient(#02196e, #7084c2 48%, #10246e 72%, #000a58); }
  .ring--amber  { left: 646px; top: 502px; background: linear-gradient(#f0cf43, #fff6c8 55%, #c9a845); }
  .ring--fern   { left: 85px;  top: 730px; background: linear-gradient(#087540, #93c27d 52%, #0a7a3e); }
  .ring--ochre  { left: 646px; top: 736px; background: radial-gradient(ellipse 170px 200px at 50% 55%, #a4665e 80%, #8b1a1e 100%); }

  .ring__line {
    position: absolute;
    height: 6px;
    width: 155px;
    background: linear-gradient(var(--gold-light), var(--gold));
  }
  .ring__line--left  { left: 0; }
  .ring__line--right { right: 0; }
  .ring__line--upper { top: 84px; }
  .ring__line--lower { top: 108px; }

  .ring__crown {
    position: absolute;
    left: 153px;
    top: 8px;
    width: 164px;
    height: 34px;
    border-radius: 0 0 40px 40px;
    background: linear-gradient(var(--crown-top), var(--crown-bottom));
  }
  .ring__star {
    position: absolute;
    top: 40px;
    width: 26px;
    height: 26px;
    border-radius: 50%;
    background: radial-gradient(#fffbe0, #d4ae2a);
  }
  .ring__star--left  { left: 115px; }
  .ring__star--right { right: 115px; }

  .ring__brand {
    position: absolute;
    left: 0; right: 0;
    top: 70px;
    text-align: center;
    font-size: 44px;
    line-height: 52px;
    letter-spacing: 2px;
    color: var(--gold-text);
  }
  .ring__name {
    position: absolute;
    left: 0; right: 0;
    top: 138px;
    text-align: center;
    font-size: 21px;
    line-height: 26px;
    letter-spacing: 4px;
    white-space: nowrap;
    color: var(--gold-text);
  }
  .ring--amber .ring__name,
  .ring--amber .ring__brand { color: var(--brown-text); }
</style>
</head>
<body>
<main class="sheet">
  <section class="ring ring--umber">
    <div class="ring__crown" role="img" aria-label="Gold crown ornament"></div>
    <div class="ring__star ring__star--left" role="img" aria-label="Gold star ornament"></div>
    <div class="ring__star ring__star--right" role="img" aria-label="Gold star ornament"></div>
    <div class="ring__line ring__line--left ring__line--upper"></div>
    <div class="ring__line ring__line--right ring__line--upper"></div>
    <div class="ring__line ring__line--left ring__line--lower"></div>
    <div class="ring__line ring__line--right ring__line--lower"></div>
    <p class="ring__brand">TMD</p>
    <p class="ring__name">UMBER CREST</p>
  </section>

  <section class="ring ring--pewter">
    <div class="ring__crown" role="img" aria-label="Gold crown ornament"></div>
    <div class="ring__star ring__star--left" role="img" aria-label="Gold star ornament"></div>
    <div class="ring__star ring__star--right" role="img" aria-label="Gold star ornament"></div>
    <div class="ring__line ring__line--left ring__line--upper"></div>
    <div class="ring__line ring__line--right ring__line--upper"></div>
    <div class="ring__line ring__line--left ring__line--lower"></div>
    <div class="ring__line ring__line--right ring__line--lower"></div>
    <p class="ring__brand">TMD</p>
    <p class="ring__name">PEWTER CREST</p>
  </section>

  <section class="ring ring--slate">
    <div class="ring__crown" role="img" aria-label="Gold crown ornament"></div>
    <div class="ring__star ring__star--left" role="img" aria-label="Gold star ornament"></div>
    <div class="ring__star ring__star--right" role="img" aria-label="Gold star ornament"></div>
    <div class="ring__line ring__line--left ring__line--upper"></div>
    <div class="ring__line ring__line--right ring__line--upper"></div>
    <div class="ring__line ring__line--left ring__line--lower"></div>
    <div class="ring__line ring__line--right ring__line--lower"></div>
    <p class="ring__brand">TMD</p>
    <p class="ring__name">SLATE CREST</p>
  </section>

  <section class="ring ring--amber">
    <div class="ring__crown" role="img" aria-label="Gold crown ornament"></div>
    <div class="ring__star ring__star--left" role="img" aria-label="Gold star ornament"></div>
    <div class="ring__star ring__star--right" role="img" aria-label="Gold star ornament"></div>
    <div class="ring__line ring__line--left ring__line--upper"></div>
    <div class="ring__line ring__line--right ring__line--upper"></div>
    <div class="ring__line ring__line--left ring__line--lower"></div>
    <div class="ring__line ring__line--right ring__line--lower"></div>
    <p class="ring__brand">TMD</p>
    <p class="ring__name">AMBER CREST</p>
  </section>

  <section class="ring ring--fern">
    <div class="ring__crown" role="img" aria-label="Gold crown ornament"></div>
    <div class="ring__star ring__star--left" role="img" aria-label="Gold star ornament"></div>
    <div class="ring__star ring__star--right" role="img" aria-label="Gold star ornament"></div>
    <div class="ring__line ring__line--left ring__line--upper"></div>
    <div class="ring__line ring__line--right ring__line--upper"></div>
    <div class="ring__line ring__line--left ring__line--lower"></div>
    <div class="ring__line ring__line--right ring__line--lower"></div>
    <p class="ring__brand">TMD</p>
    <p class="ring__name">FERN CREST</p>
  </section>

  <section class="ring ring--ochre">
    <div class="ring__crown" role="img" aria-label="Gold crown ornament"></div>
    <div class="ring__star ring__star--left" role="img" aria-label="Gold star ornament"></div>
    <div class="ring__star ring__star--right" role="img" aria-label="Gold star ornament"></div>
    <div class="ring__line ring__line--left ring__line--upper"></div>
    <div class="ring__line ring__line--right ring__line--upper"></div>
    <div class="ring__line ring__line--left ring__line--lower"></div>
    <div class="ring__line ring__line--right ring__line--lower"></div>
    <p class="ring__brand">TMD</p>
    <p class="ring__name">OCHRE CREST</p>
  </section>
</main>
</body>
</html>
```